Weight gainer supplement design

Looking for a design for a weight gainer /meal replacement supplement. The black plastic tub we will use has 2 spaces for sticker one around the rim approx 2.8cm tall x 30cm wideAnother around the main tub. The main sticker size will be 18cm tall by 70cm this will include the front of the product then wrap around to show the nutritional table.The brand is KRV (Kestrel vigor works) and the product will be called ALPHA MASSThe target ordience is men aged 16-35 its should have a profesional feel to it. The product comes in a black tub, the colores we would like to use are black and blue or red or gold or silver but we are open to suggestions and would like artistic imput. Are logo for KRV is attached but can be changed if the designer prefers.Attached is 1. KRV logo2. Image of similar product that comes in the same tub3 - 5 - images of similar products that we like the design of.The product is 12lbs and will be vanilla flavor. Please ask for more suggestions if needed, I have kept this description short to try and get artistic input.Thanks in advance :)

Target Market(s)

18-35 males who go to the gym

Industry/Entity Type

Fitness

Colors

Designer to choose colors to be used in the design.

Requirements
Must have
• name titan bulk, logo KRV
Should not have
• images of people

```html
<!DOCTYPE html>
<html lang="en">
<head>
<meta charset="utf-8">
<title>KRV Titan Bulk – Label</title>
<link href="https://fonts.googleapis.com/css2?family=Anton&family=Oswald:wght@400;600;700&family=Roboto+Condensed:ital,wght@0,700;1,700&display=swap" rel="stylesheet">
<style>
  :root{
    --stage:#e4e4e4;
    --paper:#f2f2f2;
    --strip:#e6e6e6;
    --charcoal:#2a2a2a;
    --ink:#1c1c1c;
    --red:#d3261b;
    --red-dark:#6e140b;
    --white:#ffffff;
    --steel:#3a3a3a;
  }
  html,body{margin:0;padding:0;}
  body{
    width:1200px;height:938px;overflow:hidden;
    background:var(--stage);
    display:flex;align-items:center;justify-content:center;
  }
  .label{width:900px;height:700px;display:block;box-shadow:0 10px 30px rgba(0,0,0,.18);}
  .brand-mark{font-family:"Anton",sans-serif;fill:var(--red);}
  .brand-name{font-family:"Roboto Condensed",sans-serif;font-weight:700;fill:var(--ink);}
  .stat-value{font-family:"Anton",sans-serif;fill:var(--red);}
  .stat-unit{font-family:"Oswald",sans-serif;font-weight:700;fill:var(--white);}
  .product-first{font-family:"Anton",sans-serif;fill:var(--steel);}
  .product-second{font-family:"Anton",sans-serif;fill:var(--red);}
  .tagline{font-family:"Roboto Condensed",sans-serif;font-style:italic;font-weight:700;fill:var(--white);}
  .benefit{font-family:"Oswald",sans-serif;font-weight:400;fill:var(--white);}
  .weight-text{font-family:"Oswald",sans-serif;font-weight:600;fill:var(--white);}
  .flavor{font-family:"Roboto Condensed",sans-serif;font-style:italic;font-weight:700;fill:var(--white);}
</style>
</head>
<body>
<svg class="label" viewBox="0 0 900 700" xmlns="http://www.w3.org/2000/svg">
  <defs>
    <linearGradient id="redPanel" x1="0" y1="0" x2="1" y2="1">
      <stop offset="0" stop-color="#a8241a"/>
      <stop offset="1" stop-color="#d83a26"/>
    </linearGradient>
    <linearGradient id="shadeFill" x1="0" y1="0" x2="1" y2="0">
      <stop offset="0" stop-color="#5a100a" stop-opacity="0"/>
      <stop offset="1" stop-color="#5a100a" stop-opacity=".45"/>
    </linearGradient>
    <radialGradient id="flowerFill" cx=".5" cy=".5" r=".5">
      <stop offset="0" stop-color="#f5d96b"/>
      <stop offset="1" stop-color="#f3ecd3"/>
    </radialGradient>
  </defs>

  <!-- brand panel -->
  <rect class="brand-panel" x="0" y="0" width="300" height="700" fill="var(--paper)"/>
  <polygon class="stats-panel" points="0,128 300,289 300,700 0,700" fill="var(--charcoal)"/>
  <polygon class="accent-line" points="0,120 300,281 300,291 0,130" fill="var(--red)"/>

  <text class="brand-mark" x="170" y="78" font-size="62" text-anchor="middle">KRV</text>
  <text class="brand-name" x="170" y="100" font-size="16" text-anchor="middle">Kestrel Vigor Works</text>

  <circle class="origin-badge" cx="228" cy="355" r="32" fill="var(--white)" stroke="#2c4f9e" stroke-width="4"/>

  <g class="nutrition-stats" text-anchor="middle">
    <text class="stat-value" x="228" y="457" font-size="38">25G</text>
    <text class="stat-unit" x="228" y="480" font-size="16">PROTEIN</text>
    <line x1="175" y1="496" x2="298" y2="496" stroke="#777" stroke-dasharray="3 3"/>
    <text class="stat-value" x="228" y="543" font-size="38">32G</text>
    <text class="stat-unit" x="228" y="568" font-size="16">CARBS</text>
    <line x1="175" y1="586" x2="298" y2="586" stroke="#777" stroke-dasharray="3 3"/>
    <text class="stat-value" x="228" y="628" font-size="38">280</text>
    <text class="stat-unit" x="228" y="652" font-size="15">CALORIES</text>
  </g>

  <!-- product name strip -->
  <rect class="name-strip" x="300" y="0" width="150" height="700" fill="var(--strip)"/>
  <text class="product-first" transform="translate(432 580) rotate(-90)" font-size="118" textLength="420" lengthAdjust="spacingAndGlyphs">TITAN</text>

  <circle class="weight-seal" cx="375" cy="640" r="42" fill="var(--red-dark)" stroke="var(--strip)" stroke-width="3"/>
  <text class="weight-text" x="375" y="636" font-size="15" text-anchor="middle">NT WT.</text>
  <text class="weight-text" x="375" y="656" font-size="15" text-anchor="middle">12LBS</text>

  <!-- product panel -->
  <rect class="product-panel" x="450" y="0" width="450" height="700" fill="url(#redPanel)"/>
  <rect class="shade-area" x="640" y="260" width="260" height="440" fill="url(#shadeFill)" role="img" aria-label="Soft dark tonal area"/>
  <polygon class="name-column" points="450,0 593,0 593,360 450,430" fill="var(--white)"/>
  <text class="product-second" transform="translate(574 345) rotate(-90)" font-size="112" textLength="320" lengthAdjust="spacingAndGlyphs">BULK</text>

  <rect class="tagline-band" x="593" y="0" width="47" height="425" fill="var(--red-dark)"/>
  <text class="tagline" transform="translate(625 412) rotate(-90)" font-size="23" textLength="372" lengthAdjust="spacingAndGlyphs">Advanced Muscle Mass Gainer</text>

  <g class="benefits">
    <g stroke="var(--white)" stroke-width="2.5" fill="none" stroke-linecap="round" stroke-linejoin="round">
      <path d="M470 455 l6 7 l12 -14"/>
      <path d="M470 488 l6 7 l12 -14"/>
      <path d="M470 519 l6 7 l12 -14"/>
    </g>
    <text class="benefit" x="496" y="463" font-size="20">Build Muscle*</text>
    <text class="benefit" x="496" y="496" font-size="20">Boost Endurance*</text>
    <text class="benefit" x="496" y="527" font-size="20">Achieve Peak Performance*</text>
  </g>

  <g class="flavor-art" role="img" aria-label="Vanilla flower with vanilla pods">
    <ellipse cx="566" cy="598" rx="46" ry="38" fill="url(#flowerFill)"/>
  </g>
  <text class="flavor" x="570" y="668" font-size="18" text-anchor="middle">Vanilla flavor</text>
</svg>
</body>
</html>
```